Stationary (Letterhead, Business Card) for Varendo

Develop a unique and creative design for Letterhead and Business Cards for Varendo. Varendo will be a website with tips and tricks for amateur and professional photographers. The following Layouts have to be delivered:
1. Stationary/Letterhead A4 First Page
2. Business Card (Front- and back page) 85mm x 54mm

The design should be fresh and modern.

Font: Cabin (It's a open source Google font: [url removed, login to view])

Orange: HKS 8 (CMYK: 0/50/100/0)
Grey: CMYK 0/0/0/40
Black: CMYK 0/0/0/100

1. Letterhead A4 (First Page / Second Page): For easier use we want to have only the second page printed by a printer and will put all information from the first page in a word/pages-Layout. Please remember this if you design the letterhead. So please design a base for first and following pages which includes the logo, the name and possibly more elements which might be in color. All business information (like address etc.) can only be in black. The size is A4.

2. The business card is a double sided card in landscape format (85x54mm), no folding card, no rounded edges, no QR-code.
Frontpage: Some nice way to show the Logo and Name, derived from the original logo attached, probably on an orange background!
Backpage: Lot of white space, the Logo with the Company Name and the following information:

Varendo GmbH
Lindqvistweg 12
28391 Hallbergen

[url removed, login to view] (if not on front page)

Tobias Wendler (Name of the holder of the business card)
Geschäftsführender Gesellschafter (Job title)
+49 (3829) 52093716 (Telephone)
+49 (382) 6185 2049 (Mobile)
[url removed, login to view]@[url removed, login to view]

I added (German) print infos for both Letterhead and Business Cards.

Do you have any questions? Just ask :-) Looking forward to your ideas!

```html
<!DOCTYPE html>
<html lang="de">
<head>
<meta charset="utf-8">
<title>Varendo – Geschäftsausstattung</title>
<link rel="stylesheet" href="https://fonts.googleapis.com/css2?family=Cabin:wght@400;500&display=swap">
<style>
  :root {
    --orange: #f39214;
    --grey: #a7a9ac;
    --black: #111111;
    --paper: #ffffff;
    --stage: #ffffff;
    --edge: #5a5a5a;
    --card-edge: #8a8a8a;
  }
  * { box-sizing: border-box; margin: 0; padding: 0; }
  html, body {
    width: 958px; height: 1200px; overflow: hidden;
    background: var(--stage);
    font-family: "Cabin", Arial, sans-serif;
  }
  .stage { position: relative; width: 958px; height: 1200px; }

  /* Letterhead */
  .letterhead {
    position: absolute; left: 133px; top: 46px; width: 791px; height: 1118px;
    background: var(--paper); border: 1px solid var(--edge);
  }
  .letterhead__brand {
    position: absolute; left: 34px; top: 116px;
    display: flex; align-items: center; gap: 10px;
    font-size: 36px; color: var(--grey); letter-spacing: 0.5px;
  }
  .brand-square { display: inline-block; background: var(--orange); }
  .letterhead__brand .brand-square { width: 16px; height: 16px; }
  .letterhead__contact {
    position: absolute; right: 37px; top: 24px; text-align: right;
    font-size: 9px; line-height: 12px; color: var(--grey);
  }
  .letterhead__contact .holder { font-size: 14px; line-height: 22px; color: var(--black); font-weight: 500; }
  .label { color: var(--black); }
  .letterhead__legal {
    position: absolute; right: 37px; bottom: 40px; text-align: right;
    font-size: 13.5px; line-height: 16px; color: var(--grey);
  }
  .letterhead__legal .gap { height: 16px; }
  .corner-square { position: absolute; left: 0; bottom: 0; background: var(--orange); }
  .letterhead .corner-square { width: 82px; height: 82px; }

  /* Business cards */
  .card {
    position: absolute; left: 31px; width: 320px; height: 203px;
    background: var(--paper); border: 1px solid var(--card-edge);
    box-shadow: 18px 14px 16px rgba(0,0,0,0.18);
  }
  .card--front { top: 385px; }
  .card--back { top: 612px; }
  .card--front .corner-square { width: 39px; height: 39px; }
  .card-front__brand {
    position: absolute; left: 92px; top: 82px;
    display: flex; align-items: center; gap: 7px;
    font-size: 26px; color: var(--orange);
  }
  .card-front__brand .brand-square { width: 12px; height: 12px; }

  .card-back__holder {
    position: absolute; right: 21px; top: 32px; text-align: right;
  }
  .card-back__holder .holder { font-size: 12.5px; line-height: 15px; color: var(--black); font-weight: 500; }
  .card-back__holder .role { font-size: 7.5px; line-height: 10px; color: var(--grey); }
  .card-back__contact {
    position: absolute; right: 21px; top: 89px; text-align: right;
    font-size: 7.5px; line-height: 10.5px; color: var(--grey);
  }
  .card-back__company {
    position: absolute; right: 21px; top: 150px; text-align: right;
    font-size: 7.5px; line-height: 10.5px; color: var(--grey);
  }
  .card-back__company .label { font-size: 8px; }
  .card-back__brand {
    position: absolute; left: 17px; top: 152px;
    display: flex; align-items: center; gap: 5px;
    font-size: 14px; color: var(--grey);
  }
  .card-back__brand .brand-square { width: 7px; height: 7px; }
</style>
</head>
<body>
<main class="stage">

  <section class="letterhead" aria-label="Briefbogen">
    <div class="letterhead__brand"><span class="brand-square"></span>varendo</div>

    <address class="letterhead__contact" style="font-style:normal">
      <div class="holder">Tobias Wendler</div>
      <div><span class="label">T:</span> +49 (3829) 52093716</div>
      <div><span class="label">M:</span> +49 (382) 6185 2049</div>
      <div><span class="label">E:</span> tobias.wendler@varendo.com</div>
      <div><span class="label">W:</span> varendo.com</div>
      <div><span class="label">Varendo GmbH</span> Lindqvistweg 12 &nbsp;28391 Hallbergen</div>
    </address>

    <div class="letterhead__legal">
      <div>Nordhafen Bank AG</div>
      <div><span class="label">Konto:</span> 5209 3716 2</div>
      <div><span class="label">BLZ:</span> 380 512 64</div>
      <div><span class="label">IBAN:</span> DE27 3805 1264 5209 3716 02</div>
      <div><span class="label">BIC:</span> NHBADEHHXXX</div>
      <div class="gap"></div>
      <div>Geschäftsführer: <span class="label">Tobias Wendler</span></div>
      <div>Amtsgericht Hallbergen HRB 5209 3716</div>
      <div><span class="label">UStIdNr:</span> DE520937160</div>
    </div>

    <div class="corner-square"></div>
  </section>

  <section class="card card--front" aria-label="Visitenkarte Vorderseite">
    <div class="card-front__brand"><span class="brand-square"></span>varendo</div>
    <div class="corner-square"></div>
  </section>

  <section class="card card--back" aria-label="Visitenkarte Rückseite">
    <div class="card-back__holder">
      <div class="holder">Tobias Wendler</div>
      <div class="role">Geschäftsführender Gesellschafter</div>
    </div>
    <div class="card-back__contact">
      <div><span class="label">T:</span> +49 (3829) 52093716</div>
      <div><span class="label">M:</span> +49 (382) 6185 2049</div>
      <div><span class="label">E:</span> tobias.wendler@varendo.com</div>
      <div><span class="label">W:</span> varendo.com</div>
    </div>
    <div class="card-back__brand"><span class="brand-square"></span>varendo</div>
    <div class="card-back__company">
      <div class="label">Varendo GmbH</div>
      <div>Lindqvistweg 12</div>
      <div>28391 Hallbergen</div>
    </div>
  </section>

</main>
</body>
</html>
```